Hockey Sponsorship Proposal

We are looking for a sponsorship proposal design for an apparel company to supply our hockey camps with jerseys and apparel. We want to use lots of visuals so potential business partners can see the exposure and publicity their company could get by working with us. We would like the primary colors to be red, black and white. We have attached a bunch of images but not all need to be used. We would like to see a mix of images with adult players and youth players where appropriate. Although I have provided a rough outline for the information on the powerpoint the text and images can be displayed however you would like.

Here is a link to some proposals to give you an idea of what we are looking for
https://www.quillrack.co.uk/pin/512604837219056471/

Target Market(s)

Athletic Apparel Companies

Industry/Entity Type

It Company

Requirements
Must have
• Please note this should be suitable for web as the proposal will be emailed. This is NOT for print.
Nice to have
• I would like the first page to have a full image as the backdrop with the text over top if possible.

```html
<!DOCTYPE html>
<html lang="en">
<head>
<meta charset="utf-8">
<title>About Dorian's Camps</title>
<link rel="stylesheet" href="https://fonts.googleapis.com/css2?family=Graduate&family=Lato:wght@400;700&display=swap">
<style>
  :root {
    --red: #e0261d;
    --black: #111111;
    --ink: #2b2b2b;
    --white: #ffffff;
    --backdrop: #d9d9d9;
    --rink-blue: #2a4fc4;
    --ice: #eef1f4;
  }
  * { box-sizing: border-box; margin: 0; padding: 0; }
  html, body { width: 1200px; height: 1200px; overflow: hidden; }
  body {
    background: var(--backdrop);
    font-family: "Lato", Arial, sans-serif;
    color: var(--ink);
    position: relative;
  }
  .slide {
    position: absolute;
    left: 30px;
    top: 280px;
    width: 1140px;
    height: 641px;
    background: var(--white);
    overflow: hidden;
  }
  .slide-title {
    position: absolute;
    left: 28px;
    top: 46px;
    width: 480px;
    font-family: "Graduate", "Lato", serif;
    font-size: 36px;
    line-height: 1;
    letter-spacing: -1px;
    color: var(--black);
    white-space: nowrap;
    transform: scaleY(1.15);
    transform-origin: left top;
  }
  .slide-title .accent { color: var(--red); }
  .camp {
    position: absolute;
    left: 29px;
    width: 440px;
  }
  .camp-heading {
    font-size: 20px;
    font-weight: 400;
    color: var(--red);
    line-height: 1.1;
    padding-bottom: 6px;
    position: relative;
    margin-bottom: 14px;
  }
  .camp-heading::after {
    content: "";
    position: absolute;
    left: 0;
    bottom: 0;
    width: 118px;
    height: 2px;
    background: var(--black);
  }
  .camp-list { list-style: none; }
  .camp-list li {
    position: relative;
    padding-left: 19px;
    font-size: 13.6px;
    line-height: 17px;
    margin-bottom: 4px;
  }
  .camp-list li::before {
    content: "";
    position: absolute;
    left: 3px;
    top: 5px;
    width: 5px;
    height: 5px;
    background: var(--black);
  }
  .camp-pro { top: 114px; }
  .camp-super { top: 260px; }
  .camp-festival { top: 442px; }
  .more-info {
    position: absolute;
    left: 32px;
    top: 581px;
    font-size: 11.5px;
    display: flex;
    align-items: center;
    gap: 6px;
  }
  .more-info .lead {
    padding-bottom: 3px;
    border-bottom: 1.5px solid var(--black);
  }
  .more-info .site {
    display: flex;
    align-items: center;
    gap: 4px;
    font-weight: 700;
    color: var(--black);
    padding-bottom: 3px;
  }
  .more-info .dot {
    width: 9px; height: 9px; border-radius: 50%;
    background: var(--red);
  }
  .camp-photo {
    position: absolute;
    left: 540px;
    top: 34px;
    width: 565px;
    height: 580px;
    background: linear-gradient(180deg, var(--rink-blue) 0%, #3d63d0 30%, #e8e6d8 45%, var(--ice) 75%, #cfd4da 100%);
  }
  .accent-bands {
    position: absolute;
    left: 0; top: 0;
    width: 1140px; height: 641px;
    pointer-events: none;
  }
</style>
</head>
<body>
  <section class="slide">
    <h1 class="slide-title">ABOUT <span class="accent">DORIAN'S</span> CAMPS</h1>

    <div class="camp camp-pro">
      <h2 class="camp-heading">HALVARD PRO CAMP</h2>
      <ul class="camp-list">
        <li>Held annually in August in Naples,<br>Florida.</li>
        <li>2017 camp featured 44 PHL players.</li>
        <li>Participants included Ari Castellan, Pierce Tolland,<br>Jonah Rensler, Luc Marchetti and many more.</li>
      </ul>
    </div>

    <div class="camp camp-super">
      <h2 class="camp-heading">HALVARD SUPER 64</h2>
      <ul class="camp-list">
        <li>Dorian's premiere youth hockey event.</li>
        <li>Elite camp featuring 64 of the best<br>players in North America across several age groups.</li>
        <li>Super 64 Camps held annually in<br>Vancouver &amp; Toronto.</li>
        <li>Servicing over 400 top youth hockey players</li>
      </ul>
    </div>

    <div class="camp camp-festival">
      <h2 class="camp-heading">HALVARD FESTIVAL</h2>
      <ul class="camp-list">
        <li>Youth camp for players of all skill levels.</li>
        <li>Camps located in various cities around North<br>America.</li>
        <li>Servicing over 500 youth hockey players.</li>
      </ul>
    </div>

    <p class="more-info">
      <span class="lead">For more on Dorian please visit</span>
      <span class="site"><span class="dot"></span>halvardhockey.com</span>
    </p>

    <div class="camp-photo" role="img" aria-label="Photo of a coach on the ice addressing seated youth hockey players beside the boards, with a video screen on the glass"></div>

    <svg class="accent-bands" viewBox="0 0 1140 641" aria-hidden="true">
      <polygon points="965,506 1140,506 1140,559 930,559" fill="#5a0a08" opacity="0.55"/>
      <rect x="1105" y="506" width="35" height="53" fill="var(--red)"/>
      <polygon points="793,571 1140,571 1140,624 745,624" fill="var(--black)"/>
    </svg>
  </section>
</body>
</html>
```